Poster Design for a tea beverage brand - seasonal product "Lychee Rose Tea"

We're chain of bubble tea beverage stores, located mainly in New York, and we're looking for professional poster design for our new seasonal product - Lychee Rose Tea(Please note there's no boba in this product). Our brand spirit is to deliver the most authentic flavor of tea from Taiwan. We want the style of the poster to be lovely and energetic that targets at customers around 18-35 age group, both male and female. We would like to see an image of spring felling, expressing the freshness and tasty of our products. Attached are some posters, whose styles are similar to what we want. Also attached our current product photo and some similar product photos downloaded from website for your reference.

```html
<!DOCTYPE html>
<html lang="en">
<head>
<meta charset="UTF-8">
<title>Lychee Rose Tea – Seasonal Poster</title>
<link rel="stylesheet" href="https://fonts.googleapis.com/css2?family=Luckiest+Guy&family=Alfa+Slab+One&display=swap">
<style>
  :root {
    --bg-orange: #fca41b;
    --bg-amber: #fbb416;
    --bg-yellow: #f4e40c;
    --bg-lime: #a6e70f;
    --bg-green: #5ce911;
    --dialogue-fill: #f6b514;
    --dialogue-stroke: #3b2c12;
    --cup-white: #ffffff;
    --flavor-orange: #f8a21d;
    --flavor-green: #5ee617;
    --flavor-magenta: #f52ee0;
  }
  html, body {
    margin: 0;
    padding: 0;
    overflow: hidden;
  }
  .poster {
    position: relative;
    width: 1200px;
    height: 900px;
    overflow: hidden;
    background: linear-gradient(112deg,
      var(--bg-orange) 0%,
      var(--bg-amber) 35%,
      var(--bg-yellow) 55%,
      var(--bg-lime) 72%,
      var(--bg-green) 86%);
  }
  .dialogue {
    position: absolute;
    left: 68px;
    top: 48px;
    margin: 0;
    padding: 0;
    list-style: none;
    font-family: "Luckiest Guy", "Comic Sans MS", cursive;
    font-size: 38px;
    line-height: 57px;
    letter-spacing: 2px;
    text-transform: uppercase;
    color: var(--dialogue-fill);
    -webkit-text-stroke: 1.6px var(--dialogue-stroke);
  }
  .dialogue-line { white-space: nowrap; }
  .cup {
    position: absolute;
    left: 0;
    top: 0;
    width: 1200px;
    height: 900px;
  }
  .cup-body {
    fill: var(--cup-white);
  }
  .flavor-name {
    position: absolute;
    margin: 0;
    font-family: "Alfa Slab One", Georgia, serif;
    font-size: 52px;
    line-height: 1;
    letter-spacing: 1px;
  }
  .flavor-name span {
    position: absolute;
    white-space: nowrap;
  }
  .flavor-first { left: 740px; top: 398px; color: var(--flavor-orange); }
  .flavor-second { left: 686px; top: 490px; color: var(--flavor-green); }
  .flavor-third { left: 674px; top: 580px; color: var(--flavor-magenta); font-size: 48px; }
</style>
</head>
<body>
  <main class="poster">
    <ul class="dialogue">
      <li class="dialogue-line">1: Knock knock?</li>
      <li class="dialogue-line">2: Who's there?</li>
      <li class="dialogue-line">1: No one, you should just try a</li>
      <li class="dialogue-line">new type of tea.</li>
      <li class="dialogue-line">2:Why should I do that?</li>
      <li class="dialogue-line">1: Because you can.</li>
    </ul>

    <svg class="cup" viewBox="0 0 1200 900" role="img" aria-label="White tea cup holding the seasonal drink name">
      <polygon class="cup-body" points="543,368 1122,375 1035,855 690,840"/>
    </svg>

    <h1 class="flavor-name">
      <span class="flavor-first">Lychee</span>
      <span class="flavor-second">Rose</span>
      <span class="flavor-third">tea</span>
    </h1>
  </main>
</body>
</html>
```